Elegant Business Cards & Letterhead

We will need the following that need to be designed: Letterhead and Business Cards, there winer will be re-hired for the balance of our stationary needs. Text for the cards and letterheads:

- Corporate Card instead of name
- landline: +971 (4) 362 7041
- mobile: +971 56 2819 605
- 800TUTOR
- email: dubai@velmora-lune.com
- www.velmora-lune.com
- PO Box 387261
Address: Castellan Heights Suite 1708, Dubai UAE

Thank you

Target Market(s)

VIPs, HNWI, High-end Families.

Industry/Entity Type

Luxury Market

Font styles to use
Other font styles liked:
• as explained

Colors

Designer to choose only greyscale colors for use in the design.

Requirements
Must have
• Elegant, Simple, Luxurious, Minimalistic
Nice to have
• Luxury, Golds, Engravings,
Should not have
• Much colors, funky,

```html
<!DOCTYPE html>
<html lang="en">
<head>
<meta charset="utf-8">
<title>Velmora Lune — Stationery</title>
<link rel="stylesheet" href="https://fonts.googleapis.com/css2?family=Marcellus&family=Josefin+Sans:wght@300;400&family=Montserrat:wght@400;700&family=Poppins:wght@600&display=swap">
<style>
  :root{
    --bg:#737375;
    --bg-band:#636365;
    --ink:#231f20;
    --paper:#ffffff;
    --gold:#d9bd7f;
    --gold-light:#f1dfa6;
    --gold-dark:#b08d4c;
    --text-grey:#7b7b7b;
    --contact-grey:#555555;
    --map-grey:#ececec;
  }
  *{margin:0;padding:0;box-sizing:border-box}
  html,body{width:1200px;height:1200px;overflow:hidden;background:var(--bg)}
  .board{position:relative;width:1200px;height:1200px;overflow:hidden}
  .backdrop{position:absolute;inset:0}

  .card{position:absolute;left:89.5px;width:248.5px;height:407.5px;border-radius:13px;overflow:hidden;box-shadow:0 8px 14px rgba(0,0,0,.25)}
  .card--front{top:135.5px;background:var(--ink)}
  .card--back{top:673px;background:var(--paper)}
  .card__edge{position:absolute;left:0;top:0;bottom:0;width:15.5px;background:linear-gradient(90deg,var(--gold-light),var(--gold) 50%,var(--gold-dark))}
  .card__brand{position:absolute;left:0;right:0;padding-left:15.5px;top:52px;text-align:center;font-family:"Marcellus",serif;font-size:23.5px;color:var(--gold);letter-spacing:.3px;white-space:nowrap}
  .card__contacts{position:absolute;left:36px;top:258px;font-family:"Josefin Sans",sans-serif;font-weight:300;font-size:10.4px;color:#e6e6e6;line-height:17.4px;list-style:none}
  .card__contacts li{display:flex}
  .card__contacts .label{width:21px}
  .card__contacts .value{padding-left:0}

  .card__map{position:absolute;left:25px;top:10px;width:200px;height:385px;background:radial-gradient(ellipse at 50% 50%,var(--map-grey),rgba(236,236,236,0) 70%)}
  .card__vertical-brand{position:absolute;left:121.5px;top:203.5px;transform:translate(-50%,-50%) rotate(-90deg);font-family:"Marcellus",serif;font-size:28.5px;color:var(--ink);white-space:nowrap}
  .card__rule{position:absolute;left:140px;top:102px;width:1.2px;height:205px;background:linear-gradient(180deg,rgba(35,31,32,0),var(--ink) 20%,var(--ink) 80%,rgba(35,31,32,0))}
  .card__url{position:absolute;left:221px;top:203.5px;transform:translate(-50%,-50%) rotate(-90deg);font-family:"Josefin Sans",sans-serif;font-size:12.2px;color:var(--ink);white-space:nowrap}

  .letterhead{position:absolute;left:445px;top:135.5px;width:668px;height:945px;background:var(--paper);box-shadow:0 10px 16px rgba(0,0,0,.25)}
  .letterhead__frame{position:absolute;inset:0}
  .letterhead__brand{position:absolute;left:51px;top:30px;font-family:"Marcellus",serif;font-size:41px;color:var(--ink);letter-spacing:.4px;white-space:nowrap}
  .letterhead__contacts{position:absolute;left:490px;top:32px;font-family:"Josefin Sans",sans-serif;font-weight:300;font-size:8.8px;line-height:12.4px;color:var(--contact-grey);list-style:none}
  .letterhead__contacts li{display:flex}
  .letterhead__contacts .label{width:14px}
  .letterhead__body{position:absolute;left:74.5px;top:274px;width:518.5px;font-family:"Montserrat",sans-serif}
  .letterhead__headline{font-weight:700;font-size:23.5px;color:#868686;letter-spacing:1.2px;margin-bottom:18px}
  .letterhead__body p{font-size:12.4px;line-height:24.8px;letter-spacing:1px;color:var(--text-grey);text-align:justify;margin-bottom:24.8px}
  .letterhead__sign{position:absolute;right:75px;top:752px;font-family:"Josefin Sans",sans-serif;font-size:17.4px;color:var(--ink);letter-spacing:.5px}
  .letterhead__address{position:absolute;right:75px;top:917px;font-family:"Poppins",sans-serif;font-weight:600;font-size:8.6px;color:var(--ink);white-space:nowrap;word-spacing:1px}
  .letterhead__address span+span{margin-left:7px}
</style>
</head>
<body>
<main class="board">
  <svg class="backdrop" width="1200" height="1200" viewBox="0 0 1200 1200" aria-hidden="true">
    <polygon points="0,447 1200,106 1200,727 0,1050" fill="var(--bg-band)"/>
  </svg>

  <section class="card card--front" aria-label="Business card front">
    <div class="card__edge"></div>
    <div class="card__brand">VELMORA LUNE</div>
    <ul class="card__contacts">
      <li><span class="label">T</span><span class="value">- +971 (4) 362 7041</span></li>
      <li><span class="label">F</span><span class="value">- +971 (56) 2819 605</span></li>
      <li><span class="label">E</span><span class="value">- dubai@velmora-lune.com</span></li>
      <li><span class="label">W</span><span class="value">- www.velmora-lune.com</span></li>
      <li><span class="label">PO</span><span class="value">- 387261</span></li>
      <li><span class="label">L</span><span class="value">- Castellan Heights Suite 1708,</span></li>
      <li><span class="label"></span><span class="value">&nbsp;&nbsp;Dubai UAE</span></li>
    </ul>
  </section>

  <section class="card card--back" aria-label="Business card back">
    <div class="card__map" role="img" aria-label="Faint dotted world map in light grey"></div>
    <div class="card__vertical-brand">VELMORA LUNE</div>
    <div class="card__rule"></div>
    <div class="card__url">www.velmora-lune.com</div>
  </section>

  <section class="letterhead" aria-label="Letterhead">
    <svg class="letterhead__frame" width="668" height="945" viewBox="0 0 668 945" aria-hidden="true">
      <polygon points="0,0 668,0 668,22.4 477,22.4 464.5,4.3 0,4.3" fill="var(--ink)"/>
      <polygon points="0,914 318.6,914 332.2,934 627.8,934 616.7,915 640.3,915 652.7,934 668,934 668,945 0,945" fill="var(--ink)"/>
    </svg>
    <div class="letterhead__brand">VELMORA LUNE</div>
    <ul class="letterhead__contacts">
      <li><span class="label">T</span><span>- +971 (4) 362 7041</span></li>
      <li><span class="label">F</span><span>- +971 (56) 2819 605</span></li>
      <li><span class="label">E</span><span>- dubai@velmora-lune.com</span></li>
      <li><span class="label">W</span><span>- www.velmora-lune.com</span></li>
    </ul>
    <article class="letterhead__body">
      <h1 class="letterhead__headline">Headline</h1>
      <p>Lorem ipsum dolor sit amet, consectetur adipiscing elit. Fusce dignissim pretium consectetur. Curabitur tempor posuere massa in varius. Pellentesque viverra nibh eu vehicula mattis. Nullam porta facilisis justo, a feugiat dolor sodales sed. Vestibulum neque nisi, elementum tincidunt metus sit amet, egestas bibendum enim. Aenean a blandit elit, vel rutrum mi. Nunc dapibus turpis sed massa aliquet tincidunt.</p>
      <p>Pellentesque id neque ligula. Nullam posuere, ligula a mattis posuere, lacus nisl adipiscing nunc, eu congue justo est ut diam. Nam quam nibh, dignissim non consequat in, semper eget purus. Nulla arcu sapien, viverra vitae metus tempor, congue ornare diam.</p>
      <p>Pellentesque vel nibh tempus, ullamcorper tortor sed, bibendum augue. Phasellus sollicitudin justo et quam aliquam sollicitudin. Sed eget nibh mollis, mattis sem et, viverra nulla.</p>
    </article>
    <div class="letterhead__sign">Regards</div>
    <div class="letterhead__address"><span>PO - 387261</span><span>L - Castellan Heights Suite 1708</span><span>Dubai UAE</span></div>
  </section>
</main>
</body>
</html>
```